Playful Website Design Needed Pet Sitting and Dog Walking Business

Need a simple one page Web Design Built on WordPress.
Sections:

About Us
Services Provided
Costs
Contact Us
Intake Form (Questionnaire that goes to email)
See us in Action

Industry/Entity Type

Pet Sitting and Dog Walking

Number of Pages Required

1 page

Font styles to use
Other font styles liked:
• See the Business Card Font and use that.

Colors
EE7325
F08F49
F5BC92
FAE3D3
FDF4ED

Requirements
Must have
• See attached Logo Design, with Font's and Colors Use these as theme guide

```html
<!DOCTYPE html>
<html lang="en">
<head>
<meta charset="utf-8">
<title>Tail Trail Sitters – Pet Sitting and Dog Walking</title>
<link href="https://fonts.googleapis.com/css2?family=Mystery+Quest&family=Poppins:wght@400;500;600;700&display=swap" rel="stylesheet">
<style>
:root{
  --orange:#EE5F22;
  --orange-soft:#F08F49;
  --field:#F27E45;
  --peach:#FAE3D3;
  --cream:#FDF4ED;
  --blush:#EBD3CE;
  --green:#7BC043;
  --green-light:#93CD62;
  --yellow:#F8EE1C;
  --text:#555;
  --muted:#8b8b8b;
  --white:#fff;
  --hand:"Mystery Quest", cursive;
  --body:"Poppins", sans-serif;
}
*{box-sizing:border-box;margin:0;padding:0}
html,body{width:1200px;height:4128px;overflow:hidden;background:var(--white)}
body{position:relative;font-family:var(--body);color:var(--text)}
.abs{position:absolute}
.hand{font-family:var(--hand);color:var(--orange);font-weight:400}
.brand{display:flex;align-items:center;gap:10px;font-family:var(--hand);color:var(--green);font-size:34px}
.brand-dot{width:34px;height:34px;border-radius:50%;background:var(--yellow);flex:none}
.nav{top:30px;left:590px;display:flex;align-items:center;gap:48px;font-family:var(--hand);color:var(--orange);font-size:20px;white-space:nowrap}
.btn{display:flex;align-items:center;justify-content:center;background:var(--yellow);border-radius:30px;font-weight:700;color:#333;font-size:13px;letter-spacing:.3px}
.photo{border-radius:50%}
.hero-title{left:85px;top:255px;font-size:74px;line-height:86px}
.hero-text{left:88px;top:440px;width:410px;font-size:15px;line-height:23px}
.dots{left:88px;top:640px;display:flex;gap:10px}
.dots span{width:12px;height:12px;border-radius:50%;background:var(--peach)}
.dots span:first-child{background:var(--orange-soft)}
.section-title{left:0;width:1200px;text-align:center;font-size:62px}
.rule{height:3px;background:#ddd;width:52px}
.arrow{width:52px;height:52px;border-radius:50%;background:#f0f0f0;display:flex;align-items:center;justify-content:center}
.card{top:934px;width:241px;height:401px;background:var(--white);border-radius:12px;box-shadow:0 8px 28px rgba(0,0,0,.08);overflow:hidden;text-align:center;z-index:2}
.card-img{height:207px}
.card h3{font-family:var(--hand);color:var(--orange);font-weight:400;font-size:26px;margin-top:18px}
.card p{font-size:13px;line-height:20px;padding:0 26px;margin-top:12px}
.card hr{border:0;border-top:1px solid #eee;margin:20px 22px 0}
.card a{display:block;margin-top:18px;font-size:11px;font-weight:700;color:var(--muted);text-decoration:none}
.about-title{left:706px;top:1555px;font-size:66px;color:var(--white)}
.about-rule{left:708px;top:1640px;width:52px;height:3px;background:var(--yellow)}
.about-text{left:706px;top:1655px;width:380px;font-size:14px;line-height:24px;color:var(--white)}
.costs-title{left:88px;top:2095px;font-size:62px}
.costs-text{left:88px;top:2182px;width:260px;font-size:13.5px;line-height:23px}
.price{background:var(--white);border-radius:10px;box-shadow:0 8px 30px rgba(0,0,0,.08);padding:30px 20px}
.price.featured{border:4px solid var(--yellow)}
.price-head{display:flex;align-items:center;gap:12px;font-family:var(--hand);color:var(--orange);font-size:34px;white-space:nowrap}
.paw{width:44px;height:44px;border-radius:50%;display:flex;align-items:center;justify-content:center;flex:none}
.price ul{list-style:none;margin-top:22px}
.price li{display:flex;align-items:center;gap:9px;font-size:12.5px;margin-bottom:14px;white-space:nowrap}
.tick{width:12px;height:12px;border-radius:50%;background:#bbb;flex:none}
.form-title{left:220px;top:2505px;width:510px;text-align:center;font-size:64px;color:var(--white)}
.field{height:46px;border-radius:24px;background:var(--field);color:var(--white);font-size:13px;display:flex;align-items:center;justify-content:space-between;padding:0 26px}
.field.area{align-items:flex-start;padding-top:18px;border-radius:20px}
.tagline{left:0;width:1200px;top:3200px;text-align:center;font-size:70px;line-height:82px}
.footer-links{top:3975px;left:0;width:1200px;display:flex;justify-content:center;gap:60px;font-family:var(--hand);color:var(--orange);font-size:22px}
.footer-rule{top:4064px;left:88px;width:1022px;height:1px;background:#e6e6e6}
.copy{top:4086px;font-family:var(--hand);color:var(--orange);font-size:15px;white-space:nowrap}
</style>
</head>
<body>

<!-- Header -->
<div class="abs brand" style="left:90px;top:52px"><span class="brand-dot"></span>Tail Trail Sitters</div>
<nav class="abs nav">
  <svg width="20" height="18" viewBox="0 0 20 18"><path d="M10 1 1 9h3v8h5v-5h2v5h5V9h3z" fill="var(--green)"/></svg>
  <span>About Us</span><span>Our Services</span><span>Costs</span><span>Contact Us</span>
</nav>

<!-- Hero -->
<div class="abs photo" role="img" aria-label="Group of dogs posing together" style="left:609px;top:96px;width:624px;height:624px;background:radial-gradient(circle at 45% 55%,#c9a38c,var(--blush) 70%)"></div>
<div class="abs photo" role="img" aria-label="Beagle puppy" style="left:699px;top:109px;width:96px;height:96px;background:var(--yellow)"></div>
<div class="abs photo" style="left:490px;top:447px;width:276px;height:276px;border:3px solid var(--peach)"></div>
<div class="abs photo" role="img" aria-label="Fluffy kitten" style="left:496px;top:453px;width:264px;height:264px;background:radial-gradient(circle,#f7c9a3,var(--orange-soft) 65%)"></div>
<div class="abs photo" role="img" aria-label="White kitten" style="left:953px;top:656px;width:100px;height:100px;background:radial-gradient(circle,#e7f0e0,var(--green-light) 70%)"></div>
<h1 class="abs hand hero-title">Pet Sitting and<br>Dog Walking</h1>
<p class="abs hero-text">Aenean sollicitudin lorem quis bibendum auctor nisi elit consequat ipsum nec sagittis sem nibh.</p>
<div class="abs btn" style="left:88px;top:512px;width:145px;height:49px">CONTACT US</div>
<div class="abs dots"><span></span><span></span><span></span></div>

<!-- Services -->
<h2 class="abs hand section-title" style="top:815px">Our Services</h2>
<div class="abs rule" style="left:574px;top:898px"></div>
<svg class="abs" style="left:0;top:1270px" width="1200" height="672" viewBox="0 0 1200 672">
  <path d="M0 100 C60 10 160 -5 260 20 C420 60 520 180 700 185 C900 190 1050 110 1200 0 V672 H0Z" fill="var(--green)"/>
</svg>
<div class="abs arrow" style="left:27px;top:1011px"><svg width="12" height="12" viewBox="0 0 12 12"><path d="M8 1 3 6l5 5" stroke="#333" stroke-width="2" fill="none"/></svg></div>
<div class="abs arrow" style="left:1121px;top:1011px"><svg width="12" height="12" viewBox="0 0 12 12"><path d="M4 1l5 5-5 5" stroke="#333" stroke-width="2" fill="none"/></svg></div>

<div class="abs card" style="left:102px">
  <div class="card-img" role="img" aria-label="Woman walking a dog in the woods" style="background:linear-gradient(#6f8a4a,#4e6434)"></div>
  <h3>Pet Walking</h3><p>Aenean sollicitudin lorem quis bibendum auctor nisi elit consequat.</p><hr><a>READ MORE</a>
</div>
<div class="abs card" style="left:354px">
  <div class="card-img" role="img" aria-label="Woman training a dog outdoors" style="background:linear-gradient(#9fb07c,#6f7f52)"></div>
  <h3>Pet Training</h3><p>Aenean sollicitudin lorem quis bibendum auctor nisi elit consequat.</p><hr><a>READ MORE</a>
</div>
<div class="abs card" style="left:606px">
  <div class="card-img" role="img" aria-label="Smiling woman hugging a small dog" style="background:linear-gradient(#a47a5e,#6a4a38)"></div>
  <h3>Pet Sitting</h3><p>Aenean sollicitudin lorem quis bibendum auctor nisi elit consequat.</p><hr><a>READ MORE</a>
</div>
<div class="abs card" style="left:858px">
  <div class="card-img" role="img" aria-label="Dog running after a frisbee on grass" style="background:linear-gradient(#9fc36a,#5f8e34)"></div>
  <h3>Pet Fitness</h3><p>Aenean sollicitudin lorem quis bibendum auctor nisi elit consequat.</p><hr><a>READ MORE</a>
</div>

<!-- About -->
<div class="abs photo" style="left:0;top:1434px;width:416px;height:416px;background:var(--green-light);opacity:.8"></div>
<div class="abs photo" role="img" aria-label="Man cuddling a happy golden retriever" style="left:116px;top:1422px;width:456px;height:456px;background:radial-gradient(circle at 55% 45%,#e9dccb,#a98b72 75%)"></div>
<div class="abs photo" role="img" aria-label="Grey and white kitten" style="left:457px;top:1674px;width:192px;height:192px;background:radial-gradient(circle,#fde46a,#f2b01e 75%)"></div>
<h2 class="abs hand about-title">About us</h2>
<div class="abs about-rule"></div>
<p class="abs about-text">Aenean sollicitudin, lorem quis bibendum auctor nisi elit consequat ipsum nec sagittis sem nibh id elit Duis sed odio sit amet nibh vulputate cursus a sit amet mauris. Morbi accumsan ipsum velit. Nam nec tellus a odio tincidunt auctor a ornare odio. Sed non mauris vitae erat consequat auctor eu in elit class aptent taciti sociosqu ad litora...</p>

<!-- Costs -->
<h2 class="abs hand costs-title">Costs</h2>
<div class="abs rule" style="left:88px;top:2168px;background:var(--peach)"></div>
<p class="abs costs-text">Aenean sollicitudin lorem quis bibendum auctor nisi elit consequat ipsum nec sagittis sem nibh.</p>
<div class="abs" role="img" aria-label="Dog and cat sitting together" style="left:0;top:2290px;width:152px;height:257px;background:linear-gradient(160deg,#8a6a4f,#d9c3a5);border-radius:40% 50% 30% 20%"></div>

<div class="abs price" style="left:388px;top:2067px;width:229px;height:275px">
  <div class="price-head"><span class="paw" style="background:var(--green)"><svg width="22" height="20" viewBox="0 0 22 20"><g fill="#fff"><ellipse cx="11" cy="14" rx="6" ry="5"/><circle cx="4" cy="8" r="2.4"/><circle cx="8.5" cy="4" r="2.4"/><circle cx="13.5" cy="4" r="2.4"/><circle cx="18" cy="8" r="2.4"/></g></svg></span>8$ visit</div>
  <ul><li><span class="tick"></span>8$ per visit.2 vists a day.</li><li><span class="tick"></span>All Pets , Any Age!</li><li><span class="tick"></span>Parent Supervised</li><li><span class="tick"></span>8$ per visit.2 vists a day.</li><li><span class="tick"></span>All Pets , Any Age!</li></ul>
</div>
<div class="abs price featured" style="left:620px;top:2036px;width:258px;height:337px;padding:44px 24px 30px">
  <div class="price-head"><span class="paw" style="background:var(--yellow)"><svg width="22" height="20" viewBox="0 0 22 20"><g fill="#333"><ellipse cx="11" cy="14" rx="6" ry="5"/><circle cx="4" cy="8" r="2.4"/><circle cx="8.5" cy="4" r="2.4"/><circle cx="13.5" cy="4" r="2.4"/><circle cx="18" cy="8" r="2.4"/></g></svg></span>8$ visit</div>
  <ul><li><span class="tick"></span>8$ per visit.2 vists a day.</li><li><span class="tick"></span>All Pets , Any Age!</li><li><span class="tick"></span>Parent Supervised</li><li><span class="tick"></span>8$ per visit.2 vists a day.</li><li><span class="tick"></span>All Pets , Any Age!</li></ul>
</div>
<div class="abs price" style="left:886px;top:2067px;width:224px;height:275px">
  <div class="price-head"><span class="paw" style="background:var(--orange)"><svg width="22" height="20" viewBox="0 0 22 20"><g fill="#fff"><ellipse cx="11" cy="14" rx="6" ry="5"/><circle cx="4" cy="8" r="2.4"/><circle cx="8.5" cy="4" r="2.4"/><circle cx="13.5" cy="4" r="2.4"/><circle cx="18" cy="8" r="2.4"/></g></svg></span>8$ visit</div>
  <ul><li><span class="tick"></span>8$ per visit.2 vists a day.</li><li><span class="tick"></span>All Pets , Any Age!</li><li><span class="tick"></span>Parent Supervised</li><li><span class="tick"></span>8$ per visit.2 vists a day.</li><li><span class="tick"></span>All Pets , Any Age!</li></ul>
</div>

<!-- Intake form -->
<svg class="abs" style="left:80px;top:2440px" width="780" height="700" viewBox="0 0 780 700">
  <path d="M150 650 C60 620 30 520 30 440 V230 C30 100 200 6 360 6 C560 6 730 110 730 330 C730 500 620 560 520 600 C420 640 300 690 150 650Z" fill="var(--peach)" opacity=".7" transform="translate(22 18)"/>
  <path d="M140 630 C50 600 10 500 10 420 V220 C10 90 180 0 350 0 C550 0 720 100 720 320 C720 490 610 540 510 580 C410 620 290 670 140 630Z" fill="var(--orange)"/>
</svg>
<div class="abs" role="img" aria-label="Golden retriever puppy sitting" style="left:737px;top:2515px;width:416px;height:625px;background:radial-gradient(ellipse at 50% 45%,#f3dcb4,#e0b77c 55%,rgba(255,255,255,0) 72%)"></div>
<h2 class="abs hand form-title">Intake form</h2>
<div class="abs rule" style="left:449px;top:2583px;background:#f7a57a"></div>
<div class="abs field" style="left:221px;top:2619px;width:248px">Enter name here</div>
<div class="abs field" style="left:481px;top:2619px;width:249px">Pet name</div>
<div class="abs field" style="left:221px;top:2679px;width:248px">Pet type<svg width="10" height="6"><path d="M1 1l4 4 4-4" stroke="#fff" fill="none" stroke-width="1.5"/></svg></div>
<div class="abs field" style="left:481px;top:2679px;width:249px">Breed</div>
<div class="abs field" style="left:221px;top:2739px;width:248px">Select date<svg width="10" height="6"><path d="M1 1l4 4 4-4" stroke="#fff" fill="none" stroke-width="1.5"/></svg></div>
<div class="abs field" style="left:481px;top:2739px;width:249px">Enter address</div>
<div class="abs field area" style="left:221px;top:2800px;width:513px;height:119px">Type your text</div>
<div class="abs btn" style="left:428px;top:2968px;width:144px;height:49px;font-size:17px">SUBMIT</div>

<!-- Tagline -->
<h2 class="abs hand tagline">We Feed, Walk And Play<br>With Your Pet, Each Visit!</h2>
<div class="abs btn" style="left:529px;top:3391px;width:142px;height:47px">CONTACT US</div>

<!-- See us in action -->
<div class="abs" role="img" aria-label="Row of puppies and kittens" style="left:208px;top:3500px;width:817px;height:257px;background:linear-gradient(90deg,#8c5a3a,#8e8172,#c79a6e,#dcd6cf,#2c241f);border-radius:120px 120px 0 0;opacity:.85"></div>
<svg class="abs" style="left:0;top:3690px" width="1200" height="290" viewBox="0 0 1200 290">
  <path d="M0 270 C250 20 800 -40 1180 270 C820 40 320 70 0 290Z" fill="var(--yellow)"/>
</svg>
<div class="abs brand" style="left:0;width:1200px;top:3830px;justify-content:center;font-size:46px"><span class="brand-dot" style="width:42px;height:42px"></span>Tail Trail Sitters</div>

<!-- Footer -->
<nav class="abs footer-links"><span>Home</span><span>About Us</span><span>Our Services</span><span>Costs</span><span>Contact Us</span></nav>
<div class="abs footer-rule"></div>
<div class="abs copy" style="left:0;width:1200px;text-align:center">© 2022 All Rights Reserved</div>
<div class="abs copy" style="right:90px">hello@tailtrailsitters.example</div>
<div class="abs photo" style="left:1130px;top:4034px;width:54px;height:54px;background:var(--green);display:flex;align-items:center;justify-content:center">
  <svg width="26" height="22" viewBox="0 0 26 22"><path d="M13 1C6 1 1 5 1 10c0 3 2 5 4 6l-1 5 5-3c1 0 3 1 4 1 7 0 12-4 12-9S20 1 13 1z" fill="#fff"/></svg>
</div>

</body>
</html>
```